- Redesign our business card
- Logo remains unchanged
- Current business card attached

Target Market(s)

We are a property management company

Industry/Entity Type

Business

```html
<!DOCTYPE html>
<html lang="en">
<head>
<meta charset="utf-8">
<title>Harlow Property Group – Business Card</title>
<link rel="stylesheet" href="https://fonts.googleapis.com/css2?family=Source+Sans+3:wght@400;500&display=swap">
<style>
  :root {
    --card-bg: #ececec;
    --olive: #7f7d3c;
    --slate: #6b6c70;
    --sand: #dfd0a5;
    --mark: #b9b38a;
    --white: #ffffff;
    --page: #ffffff;
  }
  * { margin: 0; padding: 0; box-sizing: border-box; }
  html, body {
    width: 1180px;
    height: 1200px;
    overflow: hidden;
    background: var(--page);
    font-family: "Source Sans 3", "Myriad Pro", Arial, sans-serif;
  }
  .card {
    position: absolute;
    width: 900px;
    height: 550px;
    background: var(--card-bg);
    border-radius: 34px;
    overflow: hidden;
  }
  .card--front { left: 12px; top: 12px; }
  .card--back  { left: 268px; top: 637px; }

  .rule { position: absolute; background: var(--olive); }
  .corner { position: absolute; background: var(--slate); }

  /* front */
  .card--front .corner { left: 0; top: 0; width: 55px; height: 55px; }
  .card--front .rule--h { left: 0; top: 54px; width: 900px; height: 4px; }
  .card--front .rule--v { left: 53px; top: 0; width: 5px; height: 550px; }

  .brand-mark {
    position: absolute;
    left: 120px;
    top: 114px;
    width: 238px;
    height: 238px;
    background: var(--mark);
  }
  .brand {
    position: absolute;
    left: 123px;
    top: 374px;
    color: var(--olive);
    font-size: 44px;
    font-weight: 400;
    letter-spacing: 2.5px;
    line-height: 1;
    white-space: nowrap;
  }
  .tagline {
    position: absolute;
    left: 123px;
    top: 421px;
    color: var(--slate);
    font-size: 32px;
    font-weight: 400;
    letter-spacing: 3.3px;
    line-height: 1;
    white-space: nowrap;
  }

  /* back */
  .card--back .corner { right: 0; top: 0; width: 54px; height: 53px; }
  .card--back .rule--h { left: 0; top: 53px; width: 846px; height: 4px; }
  .card--back .rule--v { left: 841px; top: 0; width: 5px; height: 550px; }

  .panel {
    position: absolute;
    left: 52px;
    top: 57px;
    width: 792px;
    height: 440px;
    background: var(--slate);
    border-left: 5px solid var(--olive);
    border-bottom: 5px solid var(--olive);
    color: var(--white);
  }
  .person { position: absolute; left: 38px; top: 99px; }
  .person__name { font-size: 28px; font-weight: 400; line-height: 1; letter-spacing: 0.3px; }
  .person__role { font-size: 21px; margin-top: 7px; line-height: 1; }

  .contact { position: absolute; left: 38px; top: 194px; list-style: none; }
  .contact li { font-size: 21px; line-height: 31px; white-space: nowrap; letter-spacing: 0.2px; }
  .contact li::before { content: ">"; font-size: 24px; margin-right: 6px; }
  .contact .gap { margin-left: 18px; }

  .services {
    position: absolute;
    left: 38px;
    top: 362px;
    color: var(--sand);
    font-size: 22.5px;
    letter-spacing: 0.4px;
    white-space: nowrap;
  }
  .services .sep { margin: 0 10px; }
</style>
</head>
<body>
  <section class="card card--front">
    <div class="corner"></div>
    <div class="rule rule--h"></div>
    <div class="rule rule--v"></div>
    <div class="brand-mark" role="img" aria-label="Company logo symbol placeholder"></div>
    <p class="brand">HARLOW PROPERTY GROUP</p>
    <p class="tagline">STRATA MANAGEMENT SERVICES</p>
  </section>

  <section class="card card--back">
    <div class="corner"></div>
    <div class="rule rule--h"></div>
    <div class="rule rule--v"></div>
    <div class="panel">
      <div class="person">
        <p class="person__name">DANIEL HARLOW</p>
        <p class="person__role">Licensed Strata Manager</p>
      </div>
      <ul class="contact">
        <li>PO BOX 48, BROOKFIELD VALE NSW 2099</li>
        <li>12/5-19 ASHGROVE LANE FERNBURY NSW 2098</li>
        <li>T: 02 5550 1234<span class="gap">F: 02 5550 1288</span><span class="gap">M: 0400 555 017</span></li>
        <li>E: info@harlowproperty.example<span class="gap">www.harlowproperty.example</span></li>
      </ul>
      <p class="services">Strata Management<span class="sep">|</span>Community Management<span class="sep">|</span>Property Management</p>
    </div>
  </section>
</body>
</html>
```